Dovanne Luxury Landscapes

A landscape business card.

Target Market(s)

Middle aged and up. Professionals.

Industry/Entity Type

Landscape

Contact Information for Business Card

Waverley

Colors
0054AA
0677BA
7BADD7
CADEEF
E8F1F8
0094D4
00A9DD
6FCCEA
C7EBF8
E9F6FB

Requirements
Must have
• The color blue and silver be very attractive
Nice to have
• An embossed logo. A watermark of a plant or something that indicates that we are a landscape company in the background of the backside where list of services are offered. . List of services on the back.
Should not have
• Red, yellow, orange.

```html
<!DOCTYPE html>
<html lang="en">
<head>
<meta charset="utf-8">
<title>Marla Thibodeau – Business Card</title>
<link rel="stylesheet" href="https://fonts.googleapis.com/css2?family=Arimo:wght@400;700&display=swap">
<style>
  :root {
    --blue-deep: #0054AA;
    --blue-mid: #0677BA;
    --blue-sky: #00A9DD;
    --blue-bright: #0094D4;
    --blue-panel-light: #22A8E2;
    --blue-panel-dark: #1370B6;
    --silver-light: #F2F3F4;
    --silver-mid: #D8DADC;
    --silver-dark: #BDC0C3;
    --frame-white: #FFFFFF;
  }
  * { margin: 0; padding: 0; box-sizing: border-box; }
  html, body { width: 1200px; height: 686px; overflow: hidden; background: #fff; }
  .card {
    position: relative;
    width: 1200px;
    height: 686px;
    overflow: hidden;
    font-family: "Arimo", Arial, sans-serif;
    background: radial-gradient(ellipse at 78% 45%, var(--silver-light) 0%, var(--silver-mid) 60%, var(--silver-dark) 100%);
  }
  .card__blue-panel {
    position: absolute;
    left: 0; top: 0;
    width: 594px; height: 686px;
    background: linear-gradient(30deg, var(--blue-panel-light) 0%, var(--blue-bright) 45%, var(--blue-panel-dark) 100%);
  }
  .collage {
    position: absolute;
    left: 62px; top: 99px;
    width: 710px; height: 495px;
  }
  .identity {
    position: absolute;
    left: 806px; top: 111px;
    color: var(--blue-deep);
  }
  .identity__name {
    font-weight: 700;
    font-size: 58px;
    line-height: 49px;
    letter-spacing: 1.5px;
    text-transform: uppercase;
  }
  .identity__title {
    margin-top: 9px;
    font-weight: 400;
    font-size: 21px;
    letter-spacing: 1.3px;
    color: var(--blue-mid);
  }
  .contact {
    position: absolute;
    left: 0; top: 0;
    color: var(--blue-deep);
    font-size: 28px;
    line-height: 36px;
  }
  .contact__icon { position: absolute; fill: var(--blue-deep); }
  .contact__text { position: absolute; left: 881px; white-space: nowrap; }
  .contact--phone .contact__icon { left: 804px; top: 294px; width: 52px; height: 52px; }
  .contact--phone .contact__text { top: 302px; }
  .contact--web .contact__icon { left: 798px; top: 380px; width: 54px; height: 54px; }
  .contact--web .contact__text { top: 390px; }
  .contact--address .contact__icon { left: 797px; top: 468px; width: 60px; height: 72px; }
  .contact--address .contact__text { top: 468px; }
</style>
</head>
<body>
<div class="card">
  <div class="card__blue-panel"></div>

  <svg class="collage" viewBox="54 87 621 433" xmlns="http://www.w3.org/2000/svg">
    <rect x="54" y="87" width="621" height="433" fill="var(--frame-white)"/>
    <rect role="img" aria-label="Stone retaining wall in a garden" x="54" y="88" width="108" height="142" fill="#9c9a8e"/>
    <rect role="img" aria-label="Pink flower border along a lawn" x="167" y="88" width="106" height="142" fill="#5f7a4a"/>
    <rect role="img" aria-label="White daisies" x="277" y="88" width="106" height="142" fill="#5c7a3f"/>
    <rect role="img" aria-label="Pink tulips" x="386" y="88" width="102" height="142" fill="#7f9a5b"/>
    <rect role="img" aria-label="Crew building a stone wall with an excavator" x="490" y="88" width="185" height="287" fill="#a9aca4"/>
    <rect role="img" aria-label="Curving flower bed beside a house" x="54" y="233" width="108" height="133" fill="#6d7e4b"/>
    <rect role="img" aria-label="Yellow and pink flowers" x="166" y="233" width="107" height="133" fill="#8f8a3e"/>
    <rect role="img" aria-label="Backyard pool with patio and pergola" x="277" y="233" width="211" height="133" fill="#6f7370"/>
    <rect role="img" aria-label="Flower bed in front of a home" x="54" y="369" width="203" height="151" fill="#6a7858"/>
    <rect role="img" aria-label="Stone steps lit at dusk" x="260" y="369" width="206" height="151" fill="#5b5d5b"/>
    <rect role="img" aria-label="Pool terrace seen from above" x="468" y="378" width="207" height="142" fill="#7c7f74"/>
  </svg>

  <div class="identity">
    <h1 class="identity__name">Marla<br>Thibodeau</h1>
    <p class="identity__title">Red Seal Horticulturalist</p>
  </div>

  <div class="contact contact--phone">
    <svg class="contact__icon" viewBox="0 0 24 24" aria-hidden="true"><path d="M6.6 10.8c1.4 2.8 3.8 5.1 6.6 6.6l2.2-2.2c.3-.3.7-.4 1-.2 1.1.4 2.3.6 3.6.6.6 0 1 .4 1 1V20c0 .6-.4 1-1 1C10.6 21 3 13.4 3 4c0-.6.4-1 1-1h3.5c.6 0 1 .4 1 1 0 1.3.2 2.5.6 3.6.1.3 0 .7-.2 1z"/></svg>
    <span class="contact__text">902-555-TREE</span>
  </div>

  <div class="contact contact--web">
    <svg class="contact__icon" viewBox="0 0 24 24" aria-hidden="true"><path d="M12 2a10 10 0 1 0 0 20 10 10 0 0 0 0-20zm6.9 6h-2.9a15.7 15.7 0 0 0-1.4-3.6A8 8 0 0 1 18.9 8zM12 4c.8 1.2 1.5 2.5 1.9 4h-3.8c.4-1.5 1.1-2.8 1.9-4zM4.3 14a8 8 0 0 1 0-4h3.4a16 16 0 0 0 0 4H4.3zm.8 2h2.9c.3 1.3.8 2.5 1.4 3.6A8 8 0 0 1 5.1 16zM8 8H5.1a8 8 0 0 1 4.3-3.6C8.8 5.5 8.3 6.7 8 8zm4 12c-.8-1.2-1.5-2.5-1.9-4h3.8c-.4 1.5-1.1 2.8-1.9 4zm2.3-6H9.7a14.7 14.7 0 0 1 0-4h4.6a14.7 14.7 0 0 1 0 4zm.3 5.6c.6-1.1 1.1-2.3 1.4-3.6h2.9a8 8 0 0 1-4.3 3.6zm1.7-5.6a16 16 0 0 0 0-4h3.4a8 8 0 0 1 0 4h-3.4z"/></svg>
    <span class="contact__text">Dovanne.com</span>
  </div>

  <div class="contact contact--address">
    <svg class="contact__icon" viewBox="4 1.5 16 21" preserveAspectRatio="none" aria-hidden="true"><path d="M12 2a7 7 0 0 0-7 7c0 5.2 7 13 7 13s7-7.8 7-13a7 7 0 0 0-7-7zm0 9.5A2.5 2.5 0 1 1 12 6.5a2.5 2.5 0 0 1 0 5z"/></svg>
    <span class="contact__text">18B Orchard Lane,<br>Waverley, Nova Scotia,<br>B2R 4K7</span>
  </div>
</div>
</body>
</html>
```